Coming Soon page for a new fitness startup

We are a new startup based in Toronto, Canada working on a site and mobile app where people can register for athletic events such as running, cycling, triathlon, SUP, etc.

Participants will also be able to manage their clubs and team, and connect their fitness trackers so they have all their fitness data and friends in one place.

I like very simple designs and lots of whitespace. So no need for icons or unnecessary graphics.

I prefer having a mobile phone app instead of a hero image. No need to worry about the details within the mobile app for now, we can fill it in later. Here are some landing pages that I like.
https://pixelvault.example/torvanmelk/buckets/438197-Landing-Page

Attached is a wireframe that gives some sample content for each of the sections. Please do not take the wireframe too literally, it is only meant to illustrate the content that we are experimenting with and should give an idea of how much text will be on the page.

I have also attached the company logo files. The logo is not being used yet so feel free to simplify the logo if it doesn't look great with your design. For example, I'm ok with just the name "k7ravi" in white if that looks better.

Target Market(s)

Ages 25 to 45. Interested in running, cycling, triathlon, SUP, etc.

Industry/Entity Type

Fitness

Coding

Coded - Design and coding required

Number of Pages Required

1 page

Requirements
Should not have
• Any photos should not contain track and field events, or people in a gym. Any photos should have people running or cycling outdoors. I know that photos can be easily swapped out but it is distracting to review a design that has the wrong photos.

```html
<!DOCTYPE html>
<html lang="en">
<head>
<meta charset="utf-8">
<title>k7ravi – Coming Soon</title>
<link href="https://fonts.googleapis.com/css2?family=Lato:wght@400;700&display=swap" rel="stylesheet">
<style>
  :root {
    --brand-red: #d31f36;
    --card-red: #f0575a;
    --ink: #161616;
    --logo-grey: #4d4d4f;
    --page-bg: #f9f9f9;
    --white: #ffffff;
    --banner-dark: #5a2a2c;
    --banner-warm: #b0706a;
  }
  * { margin: 0; padding: 0; box-sizing: border-box; }
  html, body { width: 1054px; height: 1200px; overflow: hidden; }
  body {
    position: relative;
    background: var(--page-bg);
    font-family: "Lato", sans-serif;
    color: var(--ink);
  }
  .waves { position: absolute; left: 0; top: 0; }

  .hero-name {
    position: absolute; left: 112px; top: 96px;
    font-size: 48px; font-weight: 700; color: var(--logo-grey); letter-spacing: 1px; line-height: 1;
  }
  .hero-title {
    position: absolute; left: 110px; top: 188px;
    font-size: 19.5px; font-weight: 400; letter-spacing: 1.6px; line-height: 23px;
    text-transform: uppercase;
  }
  .hero-subtitle {
    position: absolute; left: 110px; top: 246px;
    font-size: 14px; font-weight: 400; letter-spacing: .2px;
  }
  .hero-copy {
    position: absolute; left: 110px; top: 286px; width: 330px;
    font-size: 12.5px; line-height: 15px;
  }
  .signup { position: absolute; left: 109px; top: 340px; display: flex; gap: 7px; }
  .signup__input {
    width: 242px; height: 32px; border: 1.5px solid var(--ink); background: var(--white);
    font: 400 11px "Lato", sans-serif; padding-left: 15px; color: var(--ink);
  }
  .signup__input::placeholder { color: var(--ink); }
  .signup__button {
    width: 83px; height: 31px; border: 0; background: var(--brand-red); color: var(--white);
    font: 700 14px "Lato", sans-serif;
  }

  .app-preview__back {
    position: absolute; left: 625px; top: 176px; width: 124px; height: 248px;
    background: linear-gradient(180deg, #f4f4f4 0%, #d9d6d2 50%, #f0f0f0 100%);
    border: 1px solid #dddddd;
  }
  .app-preview__front {
    position: absolute; left: 748px; top: 108px; width: 163px; height: 338px; border-radius: 24px;
    background: linear-gradient(180deg, #faf8f5 0%, #d8d4cf 50%, #f4f2ef 100%);
    border: 3px solid #e6d9c8;
  }

  .launch {
    position: absolute; left: 0; width: 1071px; top: 470px;
    text-align: center; color: var(--white); font-size: 19px;
  }
  .launch-actions { position: absolute; left: 334px; top: 510px; display: flex; gap: 5px; }
  .launch-actions__item {
    width: 122px; height: 26px; border: 1px solid var(--white); color: var(--white);
    font-size: 11px; font-weight: 700; display: flex; align-items: center; justify-content: center;
  }

  .event-pitch { position: absolute; left: 136px; top: 658px; }
  .event-pitch__title { color: var(--brand-red); font-size: 19px; font-weight: 400; letter-spacing: .3px; }
  .event-pitch__list { list-style: none; margin-top: 18px; font-size: 12.6px; }
  .event-pitch__list li { position: relative; padding-left: 27px; line-height: 21.5px; margin-bottom: 5px; width: 310px; }
  .event-pitch__list li:last-child { margin-top: 9px; }
  .event-pitch__list li::before {
    content: ""; position: absolute; left: 2px; top: 6px; width: 10px; height: 10px; border-radius: 50%;
    background: var(--brand-red); box-shadow: 0 0 0 1.5px var(--white), 0 0 0 2.5px #e8a0a8;
  }
  .event-card__back {
    position: absolute; left: 613px; top: 666px; width: 281px; height: 211px;
    background: var(--card-red); border-radius: 8px;
  }
  .event-card__photo {
    position: absolute; left: 630px; top: 651px; width: 282px; height: 212px; border-radius: 8px;
    background: linear-gradient(120deg, #7b8692 0%, #c9cfd4 45%, #e9ecee 75%, #d5d9dc 100%);
    box-shadow: 0 6px 14px rgba(0,0,0,.25);
  }

  .cta-banner {
    position: absolute; left: 0; top: 963px; width: 1054px; height: 194px;
    background: linear-gradient(90deg, var(--banner-dark) 0%, var(--banner-warm) 40%, #c99b93 70%, #8a4a4c 100%);
  }
  .cta-banner__text {
    position: absolute; left: 0; width: 1090px; top: 1017px; text-align: center;
    color: var(--white); font-size: 19px; text-shadow: 0 1px 3px rgba(0,0,0,.3);
  }
  .cta-banner__button {
    position: absolute; left: 492px; top: 1065px; width: 107px; height: 37px;
    background: var(--brand-red); color: var(--white); font-size: 14px;
    display: flex; align-items: center; justify-content: center;
  }

  .site-footer {
    position: absolute; left: 0; top: 1158px; width: 1054px; height: 42px;
    background: var(--brand-red); color: var(--white); font-size: 11.5px; font-weight: 700;
  }
  .site-footer__link { position: absolute; top: 14px; }
  .site-footer__social { position: absolute; left: 481px; top: 14px; display: flex; gap: 18px; }
  .site-footer__social span { width: 14px; height: 14px; border-radius: 50%; background: var(--white); }
  .site-footer__copy { position: absolute; right: 86px; top: 15px; }
</style>
</head>
<body>

<svg class="waves" width="1054" height="960" viewBox="0 0 1054 960" aria-hidden="true">
  <path d="M0 0 H620 C 470 22 360 48 220 48 C 120 48 50 36 0 28 Z" fill="var(--brand-red)"/>
  <path d="M0 382 C 180 420 380 440 560 428 C 760 414 900 384 1054 388 V 580 C 1010 640 960 690 905 700 C 830 680 760 640 620 596 C 430 540 210 524 0 560 Z" fill="var(--brand-red)"/>
</svg>

<div class="hero-name">k7ravi</div>
<h1 class="hero-title">Connect your training, friend,<br>and events in one place.</h1>
<p class="hero-subtitle">A New Fitness Community is Coming Soon</p>
<p class="hero-copy">Join our email list. A referal program is coming and you’ll want to be the first know.</p>
<form class="signup">
  <input class="signup__input" type="email" placeholder="email address">
  <button class="signup__button" type="button">Notify me</button>
</form>

<div class="app-preview__back" role="img" aria-label="Mobile app feed screen"></div>
<div class="app-preview__front" role="img" aria-label="Mobile app feed screen on a phone"></div>

<p class="launch">Launching Spring 2018</p>
<div class="launch-actions">
  <span class="launch-actions__item">Sign up for events.</span>
  <span class="launch-actions__item">Invite your friends.</span>
  <span class="launch-actions__item">Connect your workouts</span>
</div>

<section class="event-pitch">
  <h2 class="event-pitch__title">ORGANIZING AN EVENT ?</h2>
  <ul class="event-pitch__list">
    <li>Attacting participants&nbsp; is hard work</li>
    <li>An online presencerequired&nbsp; effort and planning</li>
    <li>Mobile apps are costly and require a tech team</li>
    <li>Ads, landing pages, A/B testing, funnel optimization,<br>all require expertise</li>
  </ul>
</section>
<div class="event-card__back"></div>
<div class="event-card__photo" role="img" aria-label="Two men planning an event at a whiteboard"></div>

<div class="cta-banner" role="img" aria-label="Smiling group of athletes"></div>
<p class="cta-banner__text">Lets our team of experts take care of this for you. best of all, it’s no cost to yoy!</p>
<a class="cta-banner__button">Contas us</a>

<footer class="site-footer">
  <span class="site-footer__link" style="left:88px">About Us</span>
  <span class="site-footer__link" style="left:153px">Developers</span>
  <span class="site-footer__link" style="left:235px">Careers</span>
  <span class="site-footer__link" style="left:299px">Contact</span>
  <div class="site-footer__social" aria-label="Social links"><span></span><span></span><span></span></div>
  <span class="site-footer__copy">© 2018 k7ravi Inc.</span>
</footer>

</body>
</html>
```